RTV CRAFTED

building services
decks
pergola
renovation
extensions
general building

Target Market(s)

middle to upper class

Industry/Entity Type

building

Contact Information for Business Card

my details 0427839152 pkharlow47@mailvane.net BLD574926

Font styles to use
Serif

Colors
00AB8E
00BBA5
67D7C9
C6EFE9
E9F9F6

Requirements
Must have
• logo on the front and details on the back
Nice to have
• sharp and clean lines

```html
<!DOCTYPE html>
<html lang="en">
<head>
<meta charset="utf-8">
<title>RTV CRAFTED – Business Card</title>
<link href="https://fonts.googleapis.com/css2?family=Lora:wght@400;700&display=swap" rel="stylesheet">
<style>
  :root {
    --page-bg: #C6EFE9;
    --brand-teal: #00AB8E;
    --accent-teal: #00BBA5;
    --soft-teal: #67D7C9;
    --card-white: #E9F9F6;
    --ink: #14302b;
    --charcoal: #2f3a38;
    --faint-white: rgba(255, 255, 255, 0.16);
  }
  * { box-sizing: border-box; margin: 0; padding: 0; }
  html, body { width: 1200px; height: 958px; overflow: hidden; }
  body {
    background: var(--page-bg);
    font-family: "Lora", Georgia, serif;
    position: relative;
  }
  .card {
    position: absolute;
    left: 220px;
    width: 760px;
    height: 434px;
    overflow: hidden;
    box-shadow: 0 10px 26px rgba(0, 80, 70, 0.22);
  }
  /* Front */
  .card-front { top: 30px; background: var(--brand-teal); }
  .front-echo {
    position: absolute;
    left: 0; right: 0; top: 150px;
    text-align: center;
    font-size: 88px;
    font-weight: 400;
    letter-spacing: 2px;
    color: var(--faint-white);
    white-space: nowrap;
    line-height: 1;
  }
  .front-logo {
    position: absolute;
    left: 0; right: 0; top: 185px;
    text-align: center;
    font-size: 54px;
    font-weight: 400;
    letter-spacing: 3px;
    color: #ffffff;
    line-height: 1;
    white-space: nowrap;
  }
  /* Back */
  .card-back { top: 494px; background: var(--card-white); }
  .person { position: absolute; left: 40px; top: 62px; }
  .person-name { font-size: 26px; font-weight: 700; color: var(--brand-teal); line-height: 1.2; }
  .person-title { font-size: 19px; color: var(--ink); margin-top: 2px; line-height: 1.2; }
  .rule {
    position: absolute; left: 250px; top: 130px;
    width: 470px; height: 2px; background: var(--ink);
  }
  .contacts { position: absolute; left: 40px; top: 168px; }
  .contact { display: flex; align-items: center; gap: 10px; font-size: 16px; color: var(--ink); height: 27px; }
  .contact svg { width: 18px; height: 18px; flex: none; }
  .brand { position: absolute; right: 40px; top: 50px; text-align: right; }
  .brand-name { font-size: 40px; font-weight: 400; letter-spacing: 1px; color: var(--brand-teal); line-height: 1; white-space: nowrap; }
  .brand-licence { font-size: 14px; color: var(--ink); margin-top: 8px; letter-spacing: 1px; }
  .services {
    position: absolute; right: 60px; top: 258px;
    text-align: right;
  }
  .services-heading { font-size: 15px; color: var(--accent-teal); margin-bottom: 3px; padding-right: 14px; }
  .services-list {
    list-style: none; font-size: 15px; color: var(--ink); line-height: 19px;
    border-right: 2px solid var(--brand-teal);
    padding-right: 12px;
  }
  .base-strip {
    position: absolute; left: 0; bottom: 0; width: 100%; height: 14px; background: var(--charcoal);
  }
  .base-tab {
    position: absolute; right: 0; bottom: 0; width: 300px; height: 22px;
    background: var(--brand-teal); border-top-left-radius: 22px;
  }
</style>
</head>
<body>
  <section class="card card-front" aria-label="Card front">
    <div class="front-echo" aria-hidden="true">RTV CRAFTED</div>
    <h1 class="front-logo">RTV CRAFTED</h1>
  </section>

  <section class="card card-back" aria-label="Card back">
    <div class="person">
      <div class="person-name">PK Harlow</div>
      <div class="person-title">Managing Director</div>
    </div>
    <div class="rule"></div>
    <div class="contacts">
      <div class="contact">
        <svg viewBox="0 0 20 20" aria-hidden="true"><circle cx="10" cy="10" r="10" fill="#00AB8E"/><path d="M7 5.5c.6-.3 1.2.2 1.4.8l.5 1.4c.1.4-.1.8-.4 1l-.6.4c.5 1.2 1.4 2.1 2.6 2.6l.4-.6c.2-.3.6-.5 1-.4l1.4.5c.6.2 1.1.8.8 1.4-.4.9-1.3 1.4-2.2 1.2-3-.7-5.3-3-6-6-.2-.9.3-1.8 1.1-2.3z" fill="#fff"/></svg>
        <span>0427839152</span>
      </div>
      <div class="contact">
        <svg viewBox="0 0 20 20" aria-hidden="true"><circle cx="10" cy="10" r="10" fill="#00AB8E"/><rect x="5" y="6.5" width="10" height="7" rx="1" fill="#fff"/><path d="M5.5 7l4.5 3.5L14.5 7" fill="none" stroke="#00AB8E" stroke-width="1"/></svg>
        <span>pkharlow47@mailvane.net</span>
      </div>
    </div>
    <div class="brand">
      <div class="brand-name">RTV CRAFTED</div>
      <div class="brand-licence">BLD574926</div>
    </div>
    <div class="services">
      <div class="services-heading">Building Services</div>
      <ul class="services-list">
        <li>Decks</li>
        <li>Pergola</li>
        <li>Renovation</li>
        <li>Extensions</li>
        <li>General building</li>
      </ul>
    </div>
    <div class="base-strip"></div>
    <div class="base-tab"></div>
  </section>
</body>
</html>
```